DNN Website Design Project

We are going to recreate the website www.plorvenstudio.com. This is a DNN website. We like http://www.quilbarnhq.com/ and something like http://www.redstonequarryweb.com/

Look at plorvenstudio.com to see what we do, SMM, SEO and website development mostly. We have a number of video testimonials and want people to be able to contact us easily and have social media integration.

Target Market(s)

small and medium sized business owners, doctors, private practice professionals, lawyers, service pros (plumbers, electricians)

Industry/Entity Type

Media

```html
<!DOCTYPE html>
<html lang="en">
<head>
<meta charset="utf-8">
<title>Plorven Studio — Home</title>
<link href="https://fonts.googleapis.com/css2?family=Arimo:wght@400;700&family=Roboto+Condensed:wght@400&family=Comfortaa:wght@400&display=swap" rel="stylesheet">
<style>
:root{
  --red:#c40000;
  --red-dark:#8e0000;
  --red-head:#cc0000;
  --ink:#333;
  --muted:#555;
  --page:#dcdcdc;
  --panel:#fff;
  --footer-bar:#2e2e2e;
}
*{box-sizing:border-box;margin:0;padding:0}
html,body{width:1200px;height:1200px;overflow:hidden;background:var(--page)}
body{font-family:Arimo,Arial,sans-serif;color:var(--ink)}
.site{position:absolute;left:0;top:0;width:1500px;height:1500px;transform:scale(.8);transform-origin:0 0;background:var(--page)}
.abs{position:absolute}

/* header */
.topbar{left:0;top:0;width:1500px;height:50px;background:linear-gradient(#d41414,#a00000);box-shadow:0 2px 4px rgba(0,0,0,.5);z-index:3}
.brand{left:282px;top:6px;display:flex;align-items:center;gap:12px}
.brand-dot{width:40px;height:40px;border-radius:50%;background:#7a0000}
.brand-name{font-family:Comfortaa,Arial,sans-serif;font-size:22px;color:#fff}
.nav{left:665px;top:0;display:flex;height:50px}
.nav a{color:#fff;text-decoration:none;font-size:14px;line-height:50px;padding:0 18px}
.nav a.current{background:rgba(255,255,255,.18);padding:0 14px}

.stage{left:0;top:50px;width:1500px;height:445px;background:repeating-linear-gradient(90deg,#050505 0 6px,#1d1d1d 6px 10px,#0b0b0b 10px 16px);}
.stage::after{content:"";position:absolute;inset:0;background:radial-gradient(ellipse at center,rgba(60,60,60,.5),rgba(0,0,0,.6) 70%)}
.bevel{width:960px;height:28px;background:linear-gradient(#bdbdbd,#e8e8e8);clip-path:polygon(28px 0,932px 0,960px 100%,0 100%)}
.bevel-top{left:270px;top:50px;z-index:2}
.hero-frame{left:270px;top:78px;width:960px;height:389px;background:var(--panel);z-index:2}
.hero{left:20px;top:20px;width:920px;height:349px;background:var(--red);overflow:hidden}
.hero h1{position:absolute;left:34px;top:50px;font-family:"Roboto Condensed",Arial,sans-serif;font-weight:400;font-size:23px;line-height:28px;color:#fff}
.hero p{position:absolute;left:34px;top:146px;width:300px;font-size:12px;line-height:14px;color:#fff}
.btn-download{position:absolute;left:34px;top:216px;width:188px;height:47px;border-radius:4px;background:linear-gradient(#333,#000);color:#fff;font-size:13px;line-height:47px;padding-left:25px}
.btn-download svg{position:absolute;right:14px;top:14px}
.hero-visual{position:absolute;left:425px;top:37px;width:470px;height:290px;background:linear-gradient(90deg,#e8c640 0 5%,#4a8fd0 5% 11%,#8a1c30 11% 20%,#f4f4f4 20% 79%,#a6cf6c 79% 88%,#ddd 88%);border-radius:2px}
.pager{left:340px;top:326px;width:280px;height:23px;background:#eee;clip-path:polygon(20px 0,260px 0,280px 100%,0 100%)}
.dot{position:absolute;top:336px;width:15px;height:15px;border-radius:50%;background:#888;box-shadow:inset 0 1px 2px #444}
.dot.on{background:#fff;box-shadow:inset 0 1px 2px #aaa}
.bevel-bottom{left:270px;top:467px;transform:scaleY(-1);background:linear-gradient(#ddd,#aaa);z-index:2}

/* content */
.content{left:270px;top:495px;width:960px;height:778px;background:var(--panel)}
.services{left:0;top:0;width:960px;height:153px;background:linear-gradient(#f3f3f3,#e8e8e8)}
.service{position:absolute;top:32px;width:300px}
.service h3{position:absolute;left:80px;top:0;color:var(--red);font-size:18px}
.service p{position:absolute;left:80px;top:37px;width:210px;font-size:12px;line-height:14px;color:var(--muted)}
.service svg{position:absolute;left:0;top:4px}
h2.section{position:absolute;color:var(--red-head);font-size:20px;font-weight:700}
.media{position:absolute;border-radius:1px}
.body-copy{position:absolute;font-size:13px;line-height:24px;color:var(--muted)}
.btn-more{position:absolute;background:linear-gradient(#c01818,#8a0000);color:#fff;font-size:13px;text-align:center;border-radius:2px;box-shadow:0 1px 2px rgba(0,0,0,.4)}
.bubble{position:absolute;left:743px;top:236px;width:195px;height:180px;border:1px solid #ddd;background:#fcfcfc;padding:22px 18px;font-size:13px;line-height:14.6px;text-align:justify;color:var(--muted)}
.rule{position:absolute;left:25px;top:485px;width:910px;height:1px;background:#ccc}
.post{position:absolute;left:657px;width:280px}
.post .thumb{position:absolute;left:0;top:0;width:60px;height:62px;border:1px solid #ccc}
.post h4{position:absolute;left:72px;top:0;font-size:14px;color:#000;white-space:nowrap}
.post p{position:absolute;left:72px;top:17px;width:200px;font-size:12.5px;line-height:15.5px;color:var(--muted)}
.post-rule{position:absolute;left:657px;top:657px;width:278px;height:1px;background:#ccc}

/* footer */
.signup{left:270px;top:1273px;width:960px;height:67px;background:var(--footer-bar);color:#fff;font-size:13px}
.signup .lbl{position:absolute;top:27px}
.field{position:absolute;top:22px;width:147px;height:26px;background:#fff;color:#666;font-size:12px;line-height:26px;padding-left:10px}
.submit{position:absolute;left:431px;top:21px;width:58px;height:27px;border-radius:3px;background:linear-gradient(#fff,#ccc);color:#000;font-size:13px;text-align:center;line-height:27px}
.social{position:absolute;top:17px;width:31px;height:31px;border-radius:50%}
.bevel-foot{left:270px;top:1340px;background:linear-gradient(#999,#ccc)}
.footer{left:270px;top:1368px;width:960px;height:104px;background:var(--panel)}
.footer .brand{left:18px;top:22px}
.footer .brand-dot{width:58px;height:58px;background:#b44}
.footer .brand-name{color:#888;font-size:23px}
.copyright{position:absolute;right:29px;top:37px;font-size:12px;color:#444}
</style>
</head>
<body>
<div class="site">
  <header class="abs topbar">
    <div class="abs brand"><span class="brand-dot"></span><span class="brand-name">Plorven Studio, Inc.</span></div>
    <nav class="abs nav">
      <a class="current">HOME</a><a>ABOUT US</a><a>SERVICES</a><a>PRODUCTS</a><a>BLOG</a><a>CONTACT US</a>
    </nav>
  </header>

  <div class="abs stage"></div>
  <div class="abs bevel bevel-top"></div>
  <section class="abs hero-frame">
    <div class="abs hero">
      <h1>Website Development &nbsp;|&nbsp; Hosting<br>Content Management Systems &nbsp;|&nbsp; SEO<br>Pay per click advertising</h1>
      <p>sit amet, consectetur adipiscing elit. In interdum aliquet orci, vitae ornare erat elementum et.</p>
      <div class="btn-download">DOWNLOAD NOW
        <svg width="16" height="20" viewBox="0 0 16 20"><path d="M3 2l9 8-9 8" fill="none" stroke="#fff" stroke-width="3"/></svg>
      </div>
      <div class="hero-visual" role="img" aria-label="Fanned stack of sample website layouts"></div>
      <div class="abs pager"></div>
      <span class="dot on" style="left:405px"></span>
      <span class="dot" style="left:436px"></span>
      <span class="dot" style="left:467px"></span>
      <span class="dot" style="left:498px"></span>
    </div>
  </section>
  <div class="abs bevel bevel-bottom"></div>

  <main class="abs content">
    <div class="abs services">
      <div class="service" style="left:28px">
        <svg width="56" height="56" viewBox="0 0 56 56"><circle cx="28" cy="28" r="27" fill="#3a9a2a"/><circle cx="28" cy="28" r="21" fill="#fff"/><circle cx="28" cy="28" r="15" fill="#1f4fa8"/><circle cx="28" cy="28" r="9" fill="#fff"/><circle cx="28" cy="28" r="5" fill="#d01010"/></svg>
        <h3>Hosting</h3>
        <p>sit amet, consectetur adipiscing elit. In interdum aliquet orci, vitae ornare erat elementum et.</p>
      </div>
      <div class="service" style="left:343px">
        <svg width="64" height="56" viewBox="0 0 64 56"><rect x="22" y="4" width="20" height="8" rx="2" fill="none" stroke="#5a1c10" stroke-width="3"/><rect x="4" y="10" width="56" height="40" rx="4" fill="#9a2e1a"/><rect x="4" y="26" width="56" height="2" fill="#5a1c10"/><rect x="14" y="22" width="6" height="8" fill="#ccc"/><rect x="44" y="22" width="6" height="8" fill="#ccc"/></svg>
        <h3>Web Development</h3>
        <p>sit amet, consectetur adipiscing elit. In interdum aliquet orci, vitae ornare erat elementum et.</p>
      </div>
      <div class="service" style="left:648px">
        <svg width="50" height="60" viewBox="0 0 50 60"><rect x="4" y="4" width="42" height="54" rx="3" fill="#b86a30"/><rect x="8" y="8" width="34" height="46" fill="#fff"/><rect x="17" y="1" width="16" height="7" rx="2" fill="#777"/><path d="M16 16l16 28" stroke="#c00" stroke-width="2"/></svg>
        <h3>Content Management</h3>
        <p>sit amet, consectetur adipiscing elit. In interdum aliquet orci, vitae ornare erat elementum et.</p>
      </div>
    </div>

    <h2 class="section" style="left:26px;top:192px">Video</h2>
    <div class="media" style="left:25px;top:225px;width:282px;height:225px;border:1px solid #bbb;background:#eee;padding:6px">
      <div role="img" aria-label="Video preview of a website design with play button" style="width:100%;height:100%;background:linear-gradient(135deg,#f2f2f2,#e9b800 40%,#d79b00 65%,#e8eef5)"></div>
    </div>

    <h2 class="section" style="left:341px;top:192px">Why Choose Us</h2>
    <div class="media" style="left:341px;top:230px;width:282px;height:98px;border:1px solid #ccc;padding:5px">
      <div role="img" aria-label="Silhouetted group against a cloudy sky" style="width:100%;height:100%;background:linear-gradient(#d4d170,#6d6a2a 60%,#111)"></div>
    </div>
    <p class="body-copy" style="left:341px;top:340px;width:285px">Lorem ipsum dolor sit amet, consectetur adipiscing elit. In interdum aliquet orci, vitae ornare erat elementum et. Nullam sagittis quam in leo ornare ut gravida turpis eleifend.</p>
    <div class="btn-more" style="left:542px;top:446px;width:65px;height:24px;line-height:24px">More</div>

    <h2 class="section" style="left:652px;top:192px">Testimonials</h2>
    <div class="media" style="left:653px;top:232px;width:76px;height:69px;background:#444;padding:5px">
      <div role="img" aria-label="Portrait of a smiling client" style="width:100%;height:100%;background:linear-gradient(#8a8a8a,#c9a58a)"></div>
    </div>
    <div class="bubble">Lorem ipsum dolor sit amet, consectetur adipisc­ing elit, sed do eiusmod tempor incididunt ut labore et dolore magna aliqua. Ut enim ad minim veniam, quis nostrud exercitation ullamco laboris nisi ut aliquip ex ea</div>
    <div class="btn-more" style="left:867px;top:446px;width:65px;height:24px;line-height:24px">More</div>

    <div class="rule"></div>

    <h2 class="section" style="left:27px;top:523px">Welcome to Plorven Studio</h2>
    <p class="body-copy" style="left:27px;top:573px;width:595px;color:#222">Plorven Studio is a small, family-owned, full-service website development, search engine optimization and Hosting company. Since 1999, the primary goal of Plorven Studio has been to meet the needs of our clients. We believe that personally meeting with clients to determine their business philosophies offers a view into their personality, preferences and preferred techniques for approaching their target market.</p>
    <div class="btn-more" style="left:511px;top:706px;width:88px;height:33px;line-height:33px;font-size:18px">More</div>

    <h2 class="section" style="left:656px;top:521px">Hot from the blog</h2>
    <div class="post" style="top:576px">
      <div class="thumb" role="img" aria-label="Blue book illustration" style="background:linear-gradient(135deg,#c8d8f0,#3a60b0)"></div>
      <h4>Lorem ipsum dolor sit amet</h4>
      <p>Lorem ipsum dolor sit amet, consectetur adipiscing elit. In interdum aliquet orci.</p>
    </div>
    <div class="post-rule"></div>
    <div class="post" style="top:673px">
      <div class="thumb" role="img" aria-label="Glowing pumpkin illustration" style="background:radial-gradient(#f0a020,#a03010 60%,#300)"></div>
      <h4>Lorem ipsum dolor sit amet</h4>
      <p>Lorem ipsum dolor sit amet, consectetur adipiscing elit. In interdum aliquet orci.</p>
    </div>
  </main>

  <section class="abs signup">
    <span class="lbl" style="left:24px">Stay Updated:</span>
    <span class="field" style="left:118px">Name</span>
    <span class="field" style="left:273px">Email Address</span>
    <span class="submit">Submit</span>
    <span class="lbl" style="left:651px">Connect With Us:</span>
    <span class="social" style="left:782px;background:#3b6fc4"></span>
    <span class="social" style="left:820px;background:#3ab0e8"></span>
    <span class="social" style="left:858px;background:#2a7ab8"></span>
    <span class="social" style="left:896px;background:#f07818"></span>
  </section>
  <div class="abs bevel bevel-foot"></div>
  <footer class="abs footer">
    <div class="abs brand"><span class="brand-dot"></span><span class="brand-name">Plorven Studio, Inc.</span></div>
    <p class="copyright">© Copyright plorvenstudio.com . All Rights Reserved</p>
  </footer>
</div>
</body>
</html>
```